business card, stationary and envelopes for Insulation Company
Silver Otter Insulation
business card, stationary and envelopes for Insulation Company - Construction
Creative Brief
Bright & Fun-filled
Calvin Rudd
Sales Manager
7W.318 Maple Crest Drive Naperville, Illinois 60563
sales@silverotterinsulation-example.com
www.SilverOtterInsulation-example.com
Services Offered: Attic Insulation Wall Insulation Attic Ventilation Weatherization Attic Decontamination Insulation Removal Types of Insulation Cellulose Fiberglass Spray Foam Blown Batt

```html
<!DOCTYPE html>
<html lang="en">
<head>
<meta charset="utf-8">
<title>Silver Otter Insulation — Stationery Concepts</title>
<link rel="stylesheet" href="https://fonts.googleapis.com/css2?family=Nunito:wght@400;700;800&display=swap">
<style>
  :root {
    --backdrop: #3a2a1f;
    --paper: #ffffff;
    --paper-shade: #f1f1ef;
    --green: #4e7d1f;
    --green-deep: #2f5c13;
    --yellow: #e9e31c;
    --yellow-soft: #f3ee5a;
    --label: #d9cfc4;
    --ink: #5a5a5a;
    --brand: #3f6e18;
  }
  * { box-sizing: border-box; margin: 0; padding: 0; }
  html, body { width: 1200px; height: 466px; overflow: hidden; background: var(--backdrop); }
  body { position: relative; font-family: "Nunito", Arial, sans-serif; }

  .sheet { position: absolute; background: var(--paper); overflow: hidden; box-shadow: 0 2px 6px rgba(0,0,0,.45); }
  .wave { position: absolute; left: 0; bottom: 0; width: 100%; display: block; }

  .label { position: absolute; color: var(--label); font-size: 5.5px; letter-spacing: .6px; text-transform: uppercase; font-weight: 700; white-space: nowrap; }
  .section-title { left: 12px; top: 139px; font-size: 6px; }

  .brand { position: absolute; display: flex; align-items: center; gap: 3px; color: var(--brand); font-weight: 800; white-space: nowrap; line-height: 1.05; }
  .brand .mark { background: var(--green); flex: none; }

  /* business cards */
  .card { left: 12px; width: 60px; height: 38px; }
  .card-front { top: 166px; }
  .card-back { top: 252px; }
  .card .brand { font-size: 4px; left: 50%; top: 8px; transform: translateX(-50%); }
  .card .brand .mark { width: 4px; height: 4px; }
  .card-label-front { left: 16px; top: 210px; }
  .card-label-back { left: 18px; top: 297px; }

  /* letterheads */
  .letterhead { top: 31px; width: 293px; height: 394px; }
  .letterhead-one { left: 134px; }
  .letterhead-two { left: 470px; }
  .letterhead .brand { font-size: 7px; top: 18px; }
  .letterhead .brand .mark { width: 8px; height: 8px; }
  .letterhead-one .brand { left: 96px; }
  .letterhead-two .brand { left: 50%; transform: translateX(-50%); }
  .contact-block { position: absolute; left: 178px; top: 16px; font-size: 3.4px; line-height: 1.45; color: var(--ink); white-space: nowrap; }
  .footer-line { position: absolute; left: 0; right: 0; bottom: 58px; text-align: center; font-size: 3.4px; color: var(--ink); white-space: nowrap; }
  .lh-label-one { left: 252px; top: 437px; }
  .lh-label-two { left: 588px; top: 437px; }

  /* envelopes */
  .envelope-back { left: 816px; width: 341px; }
  .envelope-green { top: 31px; height: 90px; background: var(--green); }
  .envelope-green::after { content: ""; position: absolute; left: 0; right: 0; bottom: 0; height: 10px; background: var(--green-deep); }
  .envelope-yellow { top: 115px; height: 66px; background: var(--yellow); }
  .envelope-yellow::after { content: ""; position: absolute; left: 12px; right: 12px; top: 12px; bottom: 10px; background: var(--yellow-soft); }
  .envelope-white { top: 176px; height: 80px; background: var(--paper-shade); }
  .envelope-white::before { content: ""; position: absolute; left: 10px; right: 10px; top: 10px; height: 40px; border: 1px solid #d8d8d6; border-bottom: 0; }
  .env-label-two { left: 860px; top: 262px; }

  .envelope-front { left: 773px; top: 276px; width: 384px; height: 149px; }
  .envelope-front .brand { font-size: 7px; left: 14px; top: 14px; }
  .envelope-front .brand .mark { width: 8px; height: 8px; }
  .env-label-one { left: 930px; top: 437px; }
</style>
</head>
<body>

<div class="label section-title">Stationery Concepts</div>

<div class="sheet card card-front">
  <div class="brand"><span class="mark"></span>Silver Otter<br>Insulation</div>
  <svg class="wave" viewBox="0 0 100 30" height="14" preserveAspectRatio="none" aria-hidden="true">
    <path d="M0 12 C30 2 65 2 100 10 L100 30 L0 30 Z" fill="var(--yellow)"/>
    <path d="M0 16 C30 6 65 6 100 13 L100 30 L0 30 Z" fill="var(--green)"/>
  </svg>
</div>
<div class="label card-label-front">Business Card Front</div>

<div class="sheet card card-back">
  <div class="brand"><span class="mark"></span>Silver Otter<br>Insulation</div>
  <svg class="wave" viewBox="0 0 100 30" height="9" preserveAspectRatio="none" aria-hidden="true">
    <path d="M0 12 C30 2 65 2 100 10 L100 30 L0 30 Z" fill="var(--yellow)"/>
    <path d="M0 16 C30 6 65 6 100 13 L100 30 L0 30 Z" fill="var(--green)"/>
  </svg>
</div>
<div class="label card-label-back">Business Card Back</div>

<div class="sheet letterhead letterhead-one">
  <div class="brand"><span class="mark"></span>Silver Otter<br>Insulation</div>
  <div class="contact-block">
    Calvin Rudd · Sales Manager<br>
    7W.318 Maple Crest Drive<br>
    Fernbrook, Illinois 60999<br>
    sales@silverotterinsulation-example.com<br>
    www.SilverOtterInsulation-example.com
  </div>
  <svg class="wave" viewBox="0 0 290 52" height="52" preserveAspectRatio="none" aria-hidden="true">
    <path d="M0 22 C90 4 190 4 290 20 L290 52 L0 52 Z" fill="var(--yellow)"/>
    <path d="M0 28 C90 10 190 10 290 26 L290 52 L0 52 Z" fill="var(--green)"/>
    <path d="M0 40 C100 30 200 30 290 40 L290 52 L0 52 Z" fill="var(--green-deep)"/>
  </svg>
</div>
<div class="label lh-label-one">Letter Head Option 1</div>

<div class="sheet letterhead letterhead-two">
  <div class="brand"><span class="mark"></span>Silver Otter<br>Insulation</div>
  <div class="footer-line">7W.318 Maple Crest Drive Fernbrook, Illinois 60999 · sales@silverotterinsulation-example.com · www.SilverOtterInsulation-example.com</div>
  <svg class="wave" viewBox="0 0 290 52" height="52" preserveAspectRatio="none" aria-hidden="true">
    <path d="M0 22 C90 4 190 4 290 20 L290 52 L0 52 Z" fill="var(--yellow)"/>
    <path d="M0 28 C90 10 190 10 290 26 L290 52 L0 52 Z" fill="var(--green)"/>
    <path d="M0 40 C100 30 200 30 290 40 L290 52 L0 52 Z" fill="var(--green-deep)"/>
  </svg>
</div>
<div class="label lh-label-two">Letter Head Option 2</div>

<div class="sheet envelope-back envelope-green"></div>
<div class="sheet envelope-back envelope-yellow"></div>
<div class="sheet envelope-back envelope-white"></div>
<div class="label env-label-two">Envelope Option 2</div>

<div class="sheet envelope-front">
  <div class="brand"><span class="mark"></span>Silver Otter<br>Insulation</div>
  <svg class="wave" viewBox="0 0 415 40" height="36" preserveAspectRatio="none" aria-hidden="true">
    <path d="M0 16 C130 2 280 2 415 14 L415 40 L0 40 Z" fill="var(--yellow)"/>
    <path d="M0 21 C130 7 280 7 415 19 L415 40 L0 40 Z" fill="var(--green)"/>
    <path d="M0 31 C140 23 280 23 415 31 L415 40 L0 40 Z" fill="var(--green-deep)"/>
  </svg>
</div>
<div class="label env-label-one">Envelope Option 1</div>

</body>
</html>
```